Larkmoor Pawn Shop Moving

My pawn shop will be relocating on August 1st 2012. We are moving 1 block north at the corner of Dorrance and Wexcombe Ave. Next to Crumblo. The new location will include bigger facilities and shopping area. The new address is 4820 N Dorrance Rd, Halden Grove, IL 60387 555-519-GOLD (4653). I would like to see a neon light border, with dollar symbols at each corner. I would also like to print 2 per page, so thinking 8.5 x 5.5 with the design running horizontal.

```html
<!DOCTYPE html>
<html lang="en">
<head>
<meta charset="utf-8">
<title>Larkmoor Pawn Shop – We Are Moving</title>
<link rel="stylesheet" href="https://fonts.googleapis.com/css2?family=Tilt+Neon&family=Montserrat:wght@600;700;800&display=swap">
<style>
  :root {
    --wall-light: #3d3d3d;
    --wall-dark: #0e0e0e;
    --neon-red: #ff3b4e;
    --neon-red-glow: rgba(255, 30, 60, 0.85);
    --neon-green: #d8f23a;
    --neon-green-glow: rgba(190, 240, 40, 0.8);
    --ink-white: #ffffff;
  }
  html, body {
    margin: 0;
    padding: 0;
    width: 1200px;
    height: 776px;
    overflow: hidden;
    background: #000;
  }
  .flyer {
    position: relative;
    width: 1200px;
    height: 776px;
    overflow: hidden;
    font-family: "Montserrat", sans-serif;
    color: var(--ink-white);
  }
  .brick-wall {
    position: absolute;
    inset: 0;
    background: radial-gradient(ellipse 60% 55% at 50% 48%, var(--wall-light) 0%, #242424 55%, var(--wall-dark) 100%);
  }
  .neon-wire {
    position: absolute;
    inset: 0;
    width: 1200px;
    height: 776px;
    overflow: visible;
  }
  .neon-wire path {
    fill: none;
    stroke: var(--neon-red);
    stroke-width: 4;
    stroke-linecap: round;
    filter: drop-shadow(0 0 4px var(--neon-red-glow)) drop-shadow(0 0 10px var(--neon-red-glow));
  }
  .neon-red-text,
  .neon-green-text {
    font-family: "Tilt Neon", sans-serif;
    position: absolute;
    left: 0;
    width: 100%;
    text-align: center;
    margin: 0;
    line-height: 1;
  }
  .neon-red-text {
    color: var(--neon-red);
    text-shadow: 0 0 4px var(--neon-red-glow), 0 0 14px var(--neon-red-glow), 3px 4px 6px rgba(0,0,0,0.7);
  }
  .neon-green-text {
    color: var(--neon-green);
    text-shadow: 0 0 4px var(--neon-green-glow), 0 0 14px var(--neon-green-glow), 3px 4px 6px rgba(0,0,0,0.7);
  }
  .shop-name-top {
    top: 40px;
    font-size: 96px;
    letter-spacing: 2px;
  }
  .shop-name-bottom {
    top: 140px;
    font-size: 90px;
    letter-spacing: 3px;
  }
  .dollar {
    position: absolute;
    font-family: "Tilt Neon", sans-serif;
    font-size: 120px;
    line-height: 1;
    color: var(--neon-green);
    text-shadow: 0 0 4px var(--neon-green-glow), 0 0 14px var(--neon-green-glow), 3px 4px 6px rgba(0,0,0,0.7);
  }
  .dollar-tl { left: 28px;  top: 22px; }
  .dollar-tr { left: 1086px; top: 22px; }
  .dollar-bl { left: 28px;  top: 618px; }
  .dollar-br { left: 1086px; top: 618px; }
  .headline {
    position: absolute;
    left: 0;
    top: 292px;
    width: 100%;
    margin: 0;
    text-align: center;
    font-weight: 800;
    font-size: 92px;
    line-height: 1;
    letter-spacing: 1px;
    transform: rotate(-3deg);
    text-shadow: 4px 6px 8px rgba(0,0,0,0.85);
  }
  .move-date {
    position: absolute;
    left: 0;
    top: 392px;
    width: 100%;
    margin: 0;
    text-align: center;
    font-weight: 700;
    font-size: 44px;
    line-height: 1;
    color: var(--neon-green);
    text-shadow: 3px 4px 6px rgba(0,0,0,0.8);
  }
  .move-date sup {
    font-size: 24px;
    vertical-align: 18px;
  }
  .date-underline {
    position: absolute;
    left: 410px;
    top: 438px;
    width: 384px;
    height: 20px;
    overflow: visible;
  }
  .date-underline path {
    fill: none;
    stroke: var(--neon-green);
    stroke-width: 4;
    stroke-linecap: round;
    filter: drop-shadow(0 0 4px var(--neon-green-glow));
  }
  .details {
    position: absolute;
    left: 120px;
    top: 472px;
    width: 960px;
    margin: 0;
    text-align: center;
    font-weight: 600;
    font-size: 19.5px;
    line-height: 30px;
    text-shadow: 2px 3px 4px rgba(0,0,0,0.8);
  }
  .divider {
    position: absolute;
    left: 174px;
    top: 548px;
    width: 858px;
    height: 16px;
    overflow: visible;
  }
  .divider path {
    fill: none;
    stroke: var(--neon-red);
    stroke-width: 4;
    stroke-linecap: round;
    filter: drop-shadow(0 0 4px var(--neon-red-glow));
  }
  .address {
    position: absolute;
    left: 0;
    top: 582px;
    width: 100%;
    margin: 0;
    text-align: center;
    font-weight: 600;
    font-size: 36px;
    line-height: 1;
    text-shadow: 3px 4px 6px rgba(0,0,0,0.8);
  }
  .phone {
    top: 632px;
    font-size: 80px;
    letter-spacing: 1px;
  }
</style>
</head>
<body>
<main class="flyer">
  <div class="brick-wall" role="img" aria-label="Dark painted brick wall background, lit softly in the centre"></div>

  <svg class="neon-wire" viewBox="0 0 1200 776" aria-hidden="true">
    <path d="M 40 112 C 70 40, 180 30, 262 98 C 292 124, 322 134, 382 134 L 818 134 C 878 134, 918 122, 958 92 C 1028 38, 1110 42, 1152 76"/>
    <path d="M 1128 122 C 1156 300, 1140 500, 1158 660 C 1164 712, 1148 744, 1100 746 L 124 738 C 64 738, 46 716, 50 680 C 56 500, 40 300, 62 130"/>
  </svg>

  <h1 class="neon-red-text shop-name-top">LARKMOOR</h1>
  <p class="neon-green-text shop-name-bottom">PAWN SHOP</p>

  <span class="dollar dollar-tl">$</span>
  <span class="dollar dollar-tr">$</span>
  <span class="dollar dollar-bl">$</span>
  <span class="dollar dollar-br">$</span>

  <h2 class="headline">WE ARE MOVING</h2>
  <p class="move-date">AUGUST 1<sup>ST</sup> 2012</p>
  <svg class="date-underline" viewBox="0 0 384 20" aria-hidden="true">
    <path d="M 4 10 C 120 16, 260 16, 380 6"/>
  </svg>

  <p class="details">We are moving 1 block north at the corner of Dorrance and Wexcombe Ave. Next to<br>Crumblo. The new location will include bigger facilities and shopping area.</p>

  <svg class="divider" viewBox="0 0 858 16" aria-hidden="true">
    <path d="M 4 10 C 300 4, 560 4, 854 8"/>
  </svg>

  <p class="address">4820 N Dorrance Rd, Halden Grove, IL 60387</p>
  <p class="neon-green-text phone">555-519-GOLD (4653)</p>
</main>
</body>
</html>
```